Website Banners

I am working on a new website and need some banners for the main service pages. I will need 5 in total and may potentially choose from multi-designers and increase the payment or will choose the designer for all 5 based on the first one.

I am including a s the link to the development site. all the graphics in there at the moment are conceptual but give you an idea of what I am looking for.

___________________________

http://dev.morvelquist.example:8080/

On the home page I am looking for the main banner to represent an organisation moving or transitioning to the cloud but I want to use an individual (like a runner) to represent that.

I would like a text overlay for that banner to say: "Businesses don't transition themselves, so what are you waiting for?" or "Get ready for business at the speed of sound"

http://dev.morvelquist.example:8080/about-2/

On the About page I am looking for two banners. The first one to depict an Australian city street with a text overlay to say: "We stand for mid-market Australia". The second one to depict a local government/council image with a text overlay to say "We are local government and public sector experts"

http://dev.morvelquist.example:8080/about-2

On the Advisory page I am looking for a banner that depicts "trust" in a professional business sense with a text overlay to say "Challenge yourself - or have us do it for you"

http://dev.morvelquist.example:8080/consulting/

On the Consulting page I am looking for two banners. The first one to depict "getting your hands dirty" or "getting in there and getting the job done" with a text overlay to say "If you want success in your business put us there". The second one with an image to depict a competitive consulting environment with a text overlay to say "We understand we are an option but our approach is to make you a priority"

5 all up. I don't care which one you respond to.

My logo is attached.

I have also attached a couple of other designs that I have gone for in the past.

Target Market(s)

mid market (sized) businesses

Industry/Entity Type

It Service

Font styles to use
Serif

Colors
33a6d7
3176b4
f68d4d
f37122
ffffff

Requirements
Must have
• energy

```html
<!DOCTYPE html>
<html lang="en">
<head>
<meta charset="utf-8">
<title>Local Government Banner</title>
<link href="https://fonts.googleapis.com/css2?family=Oswald:wght@400;500&display=swap" rel="stylesheet">
<style>
  :root {
    --page-bg: #eeeeec;
    --brand-orange: #f37122;
    --brand-blue: #33a6d7;
    --white: #ffffff;
    --sky-deep: #1f4fc4;
    --sky: #2f62d3;
    --stone: #f4f4f2;
    --stone-shade: #9fb0ad;
    --paving: #a86b52;
    --kerb: #b9b6ae;
    --lawn: #5f7c3c;
    --mosaic: #b8a08c;
    --mosaic-dark: #8c6b62;
  }
  html, body {
    margin: 0;
    padding: 0;
    width: 1200px;
    height: 956px;
    overflow: hidden;
    background: var(--page-bg);
  }
  .canvas {
    position: relative;
    width: 1200px;
    height: 956px;
  }
  .banner {
    position: absolute;
    left: 51px;
    top: 224px;
    width: 1098px;
    height: 457px;
    overflow: hidden;
  }
  .banner-photo {
    position: absolute;
    inset: 0;
    background: linear-gradient(
      to bottom,
      var(--sky-deep) 0%,
      var(--sky) 20%,
      var(--stone) 21.5%,
      var(--stone) 30%,
      var(--stone-shade) 42%,
      var(--stone) 54%,
      var(--paving) 55.5%,
      var(--paving) 58%,
      var(--kerb) 60%,
      var(--kerb) 64%,
      var(--lawn) 66%,
      var(--lawn) 72%,
      var(--mosaic) 75%,
      var(--mosaic-dark) 100%
    );
  }
  .headline-bar {
    position: absolute;
    left: 171px;
    top: 249px;
    width: 756px;
    height: 68px;
    background: var(--brand-orange);
    display: flex;
    align-items: center;
    justify-content: center;
  }
  .headline {
    margin: 0;
    font-family: "Oswald", sans-serif;
    font-weight: 400;
    font-size: 32px;
    letter-spacing: 0.3px;
    text-transform: uppercase;
    color: var(--white);
    white-space: nowrap;
  }
  .brand-box {
    position: absolute;
    left: 401px;
    top: 317px;
    width: 312px;
    height: 63px;
    background: var(--brand-blue);
    display: flex;
    align-items: center;
    justify-content: center;
  }
  .brand-name {
    font-family: "Oswald", sans-serif;
    font-weight: 400;
    font-size: 25px;
    letter-spacing: 1px;
    color: var(--white);
    white-space: nowrap;
  }
</style>
</head>
<body>
  <main class="canvas">
    <section class="banner">
      <div class="banner-photo" role="img" aria-label="Photograph of a white colonnaded parliament building under a deep blue sky, with a flagpole frame above, a lawn and a circular pebble mosaic forecourt in front"></div>
      <div class="headline-bar">
        <h1 class="headline">We are local government and public sector experts</h1>
      </div>
      <div class="brand-box">
        <span class="brand-name">Morvelquist Advisory</span>
      </div>
    </section>
  </main>
</body>
</html>
```